Recruitment technology firm needs a downloadable pdf to generate leads.

We need design work for a downloadable pdf that will serve as an educational document to visitors to our website. We help clients identify candidates that fit their job posting. We do that by defining the personality of the job and then assessing the personality of the candidates. We then mathematically compare and rank all the candidates against the job. Our colour scheme is blue. The final design should move from communicating a lack of fit or frustration to people fitting their job and success per the text we have built. People who download this lead generator will be added to our email list for re-marketing purposes. our website is www.tallowridgeadvisory.com. I've attached an example of a lead generator (ebike)for a business unrelated to ours.

Target Market(s)

Our target market is businesses of 50-300 people, we're targeting business owners or executives of entrepreneurial (vs. corporate) companies.

Colors
85acd3
3377b5
0455a3

Requirements
Must have
• Easy to read so text isn't overwhelming.
Nice to have
• Don't be compelled to use our website photos or those like it. I'd like this to reflect entrepreneurial companies, not corporate, suit and tie companies.

```html
<!DOCTYPE html>
<html lang="en">
<head>
<meta charset="utf-8">
<title>Tallow Ridge Advisory – Hiring for Fit Brochure</title>
<link href="https://fonts.googleapis.com/css2?family=Arimo:wght@400;700&display=swap" rel="stylesheet">
<style>
:root{
  --blue-light:#85acd3;
  --blue-mid:#3377b5;
  --blue-deep:#0455a3;
  --panel:#4a6db3;
  --band:#3f6ab2;
  --number-faint:#c9d8ec;
  --axis-num:#7fa5da;
  --candidate:#8fb3dd;
  --ink:#0455a3;
  --rule:#dfe5ee;
  --paper:#ffffff;
  --backdrop:#ffffff;
}
*{box-sizing:border-box;margin:0;padding:0}
html,body{width:1200px;height:849px;overflow:hidden;background:var(--backdrop)}
body{font-family:"Arimo",Arial,sans-serif;color:var(--ink)}
.stage{position:absolute;left:0;top:0;width:2268px;height:1604px;transform:scale(0.5291);transform-origin:0 0}
.page{position:absolute;width:745px;height:1067px;background:var(--paper);box-shadow:0 2px 6px rgba(0,0,0,.18);overflow:hidden}
.page--front{left:365px;top:132px}
.page--back{left:1169px;top:132px}
.brand-band{position:absolute;left:0;width:100%;background:linear-gradient(90deg,var(--blue-light),var(--blue-mid) 55%,var(--blue-deep));color:#fff}
.brand-band--top{top:0;height:191px}
.brand-band--bottom{bottom:0;height:125px}
.brand-name{position:absolute;display:flex;align-items:center;gap:14px;font-weight:700;font-size:30px;letter-spacing:.5px;color:#fff}
.brand-name .mark{width:26px;height:26px;border-radius:50%;background:#fff}
.brand-band--top .brand-name{left:80px;top:118px}
.brand-band--bottom .brand-name{left:80px;top:48px}
.contact{position:absolute;font-size:10px;line-height:14px;color:#fff}
.contact dt{float:left;clear:left;width:40px;font-weight:700}
.contact dd{margin-left:40px}
.brand-band--top .contact{left:495px;top:112px}
.brand-band--bottom .contact{left:492px;top:40px}
.photo{position:absolute;left:0;top:247px;width:361px;height:750px;background:linear-gradient(160deg,#e9ecee 0%,#b9c6d1 35%,#6f8eaf 65%,#3f5f86 100%)}
.column-rule{position:absolute;left:376px;top:240px;width:1px;height:785px;background:var(--rule)}
.headline{font-weight:700;font-size:22px;line-height:21px;color:var(--ink);text-transform:uppercase}
.page--front .headline{position:absolute;left:414px;top:245px}
.intro-band{position:absolute;left:376px;top:309px;width:369px;height:47px;background:var(--band);color:#fff;font-weight:700;font-size:10.5px;line-height:13px;text-align:center;padding-top:10px}
.reasons{position:absolute;left:412px;top:382px;width:320px;font-size:9.6px;line-height:12.1px}
.reasons p{margin-bottom:12px}
.reason{position:relative;margin-bottom:14px}
.reason h3{font-size:9.6px;font-weight:700;text-transform:uppercase}
.reason .num{position:absolute;left:-20px;top:8px;font-size:62px;font-weight:700;color:var(--number-faint);z-index:-1;line-height:1}
.reason-list{position:relative;z-index:1}
.page--back .headline{position:absolute;left:42px}
.fit-copy{position:absolute;left:42px;top:130px;width:318px;font-size:9.6px;line-height:12.1px}
.fit-copy p{margin-bottom:12px}
.chart{position:absolute;left:389px;width:356px;height:163px;background:var(--panel);overflow:visible}
.chart--traits{top:59px}
.chart--scores{top:244px}
.chart svg{position:absolute;left:0;top:0;overflow:visible}
.chart .label{font-family:"Arimo",Arial,sans-serif;font-size:8px;font-weight:700;fill:#fff}
.chart .axis-num{font-family:"Arimo",Arial,sans-serif;font-size:28px;font-weight:700;fill:var(--axis-num)}
.divider{position:absolute;left:42px;width:663px;height:1px;background:var(--rule)}
.steps{position:absolute;left:275px;top:481px}
.step{position:absolute;top:28px;width:124px;height:80px;background:var(--panel);color:#fff;font-size:8px;font-weight:700;line-height:10px;text-transform:uppercase;padding:0 0 14px 30px;display:flex;align-items:flex-end}
.step .num{position:absolute;left:-6px;top:-36px;font-size:64px;line-height:1;font-weight:700;color:var(--number-faint)}
.quote{position:absolute;font-size:9.6px;line-height:12.1px;width:310px}
.quote cite{display:block;font-style:normal;font-size:9px}
</style>
</head>
<body>
<div class="stage">

  <section class="page page--front">
    <header class="brand-band brand-band--top">
      <div class="brand-name"><span class="mark"></span>TALLOW RIDGE</div>
      <dl class="contact">
        <dt>web</dt><dd>www.tallowridgeadvisory.com</dd>
        <dt>email</dt><dd>hello@tallowridgeadvisory.com</dd>
        <dt>phone</dt><dd>555 010 0199</dd>
      </dl>
    </header>

    <div class="photo" role="img" aria-label="Photo of a smiling professional in a denim shirt, arms crossed"></div>
    <div class="column-rule"></div>

    <h1 class="headline">5 Reasons you suck<br>at hiring for fit</h1>
    <div class="intro-band">Hiring the wrong fit is painful, we are with you there.<br>Bad hires ruin your day, every day.</div>

    <div class="reasons">
      <p>You want to make sure your next hire is the right one. You know what it’s like when you hire the wrong person – they aren’t productive, they don’t get along with others, there’s tension, you have to let them go, and you re-start the whole process over again.</p>
      <p>Our goal is to help you stop this cycle.<br>Here are 5 mistakes you are likely making:</p>
      <div class="reason-list">
        <div class="reason"><span class="num">1</span>
          <h3>You have not defined the obstacles found in the job</h3>
          Every job has its challenges and you need to find someone who will deal with the challenges as a high performer would. Spending too much time in unstructured conversation or putting too much emphasis on selling the role can detract from this key insight. Define the top 2-5 obstacles and learn how the candidate has or would tackle them.
        </div>
        <div class="reason"><span class="num">2</span>
          <h3>You describe the job using words, not data</h3>
          Detail oriented means different things to different people. You only find out after you have hired someone that they are not detailed enough (or are too detailed!). The same can happen when we say a candidate needs to be proactive or risk oriented. You only find out later that you hired too much or too little. You used words and not numbers to define what you needed for the role.
        </div>
        <div class="reason"><span class="num">3</span>
          <h3>You assume knowledge and experience equals performance</h3>
          Just because someone’s resume says they are a strong manager does not mean they are one. And yet this is how you screen and rank your candidates. The best resumes rise to the top. But resumes are a terrible predictor of performance. Success at one company does not mean success in yours. Who are you overlooking that may be a better performer? (We have an idea below.)
        </div>
        <div class="reason"><span class="num">4</span>
          <h3>You are biased and subjective in your assessment of others</h3>
          You get attracted to certain resumes and backgrounds. You make judgement calls on phone interviews. You do the same when you meet someone and during an interview. Very few recruitment processes have a way of OBJECTIVELY ranking and comparing candidates. As a result we end up picking someone we like as opposed to someone who will excel in the job.
        </div>
        <div class="reason"><span class="num">5</span>
          <h3>You think your “gut” makes good decisions</h3>
          “Gut” has more to do with how likeable someone is than how effective they will be. Effectiveness comes from a person’s ability to consistently behave in a manner that produces exceptional results. Do not make judgement calls on behaviours a candidate shows but may not be able to consistently repeat.
        </div>
      </div>
    </div>
  </section>

  <section class="page page--back">
    <h2 class="headline" style="top:58px">So how can you hire<br>for fit?</h2>
    <div class="fit-copy">
      <p>Personality is the most significant predictor of both fit to the manager and performance in the role. It is also one of the most difficult things to assess without the use of an objective tool.</p>
      <p>Most candidates behave a certain way in an interview, but it may be something that is difficult for them to sustain.</p>
      <p>To start addressing the problem of hiring bad fits you need to add more objectivity to your process. RoleMatch is a tool designed to define a benchmark of what personality is required in a role using data. Everyone gets on the same page of what success looks like.</p>
      <p>From there each candidate completes a TraitScan personality survey within the RoleMatch tool. Then they are compared equally to the benchmark and ranked objectively. All candidates are compared using the same personality dimensions.</p>
      <p>You leverage specific data and our insight to find the best candidates … Your ability to consistently hire above average fits increases … You achieve more.</p>
      <p>Here are the results of a candidate compared to a job.<br>The job is represented in white, the candidate is represented in blue.</p>
    </div>

    <div class="chart chart--traits" role="img" aria-label="Trait chart comparing job and candidate on a -2 to 2 scale">
      <svg width="356" height="180" viewBox="0 0 356 180">
        <text class="label" x="14" y="23">ASSERTIVENESS</text>
        <text class="label" x="14" y="54">SOCIABILITY</text>
        <text class="label" x="14" y="85">PACE</text>
        <text class="label" x="14" y="108">DETAIL</text>
        <text class="label" x="14" y="118">ORIENTATION</text>
        <line x1="108" y1="142" x2="320" y2="142" stroke="#fff" stroke-width="1"/>
        <g stroke="#fff"><line x1="108" y1="136" x2="108" y2="142"/><line x1="159" y1="136" x2="159" y2="142"/><line x1="214" y1="134" x2="214" y2="142"/><line x1="268" y1="136" x2="268" y2="142"/><line x1="320" y1="136" x2="320" y2="142"/></g>
        <polyline points="313,20 188,51 159,82 207,110" fill="none" stroke="var(--candidate)" stroke-width="1"/>
        <g fill="var(--candidate)"><circle cx="313" cy="20" r="5"/><circle cx="188" cy="51" r="5"/><circle cx="159" cy="82" r="5"/><circle cx="207" cy="110" r="5"/></g>
        <polyline points="302,20 269,51 108,82 194,110" fill="none" stroke="#fff" stroke-width="1"/>
        <g fill="#fff"><circle cx="302" cy="20" r="5"/><circle cx="269" cy="51" r="5"/><circle cx="108" cy="82" r="5"/><circle cx="194" cy="110" r="5"/></g>
        <g class="axis-num" text-anchor="middle"><text x="110" y="176">-2</text><text x="159" y="176">-1</text><text x="214" y="176">0</text><text x="268" y="176">1</text><text x="320" y="176">2</text></g>
      </svg>
    </div>

    <div class="chart chart--scores" role="img" aria-label="Score chart comparing job and candidate on a 0 to 9 scale">
      <svg width="356" height="180" viewBox="0 0 356 180">
        <text class="label" x="14" y="37">BEHAVIORAL</text>
        <text class="label" x="14" y="47">ADAPTABILITY</text>
        <text class="label" x="14" y="73">EMOTIVENESS</text>
        <text class="label" x="14" y="103">CREATIVITY</text>
        <line x1="96" y1="143" x2="308" y2="143" stroke="#fff"/>
        <g stroke="#fff"><line x1="96" y1="135" x2="96" y2="150"/><line x1="218" y1="137" x2="218" y2="143"/><line x1="248" y1="137" x2="248" y2="143"/><line x1="278" y1="137" x2="278" y2="143"/><line x1="308" y1="137" x2="308" y2="143"/></g>
        <polyline points="229,101 269,42 307,71" fill="none" stroke="var(--candidate)"/>
        <g fill="var(--candidate)"><circle cx="229" cy="101" r="5"/><circle cx="269" cy="42" r="5"/><circle cx="307" cy="71" r="5"/></g>
        <polyline points="218,42 218,71 218,101" fill="none" stroke="#fff"/>
        <g fill="#fff"><circle cx="218" cy="42" r="5"/><circle cx="218" cy="71" r="5"/><circle cx="218" cy="101" r="5"/></g>
        <g class="axis-num" text-anchor="middle"><text x="95" y="176">0</text><text x="218" y="176">6</text><text x="248" y="176">7</text><text x="278" y="176">8</text><text x="308" y="176">9</text></g>
      </svg>
    </div>

    <div class="divider" style="top:452px"></div>

    <h2 class="headline" style="top:482px">What’s next?</h2>
    <div class="steps">
      <div class="step" style="left:0"><span class="num">1</span>Contact us to<br>discuss your<br>position</div>
      <div class="step" style="left:136px"><span class="num">2</span>Leverage our<br>tools, process<br>and insights<br>throughout<br>your process</div>
      <div class="step" style="left:273px"><span class="num">3</span>Welcome a<br>great new team<br>member and<br>crush your<br>goals</div>
    </div>

    <div class="divider" style="top:621px"></div>

    <h2 class="headline" style="top:658px">What RoleMatch users are<br>saying</h2>

    <blockquote class="quote" style="left:404px;top:714px;width:305px">
      RoleMatch allows us to identify those that don’t fit our benchmark early so we don’t spend time with those that don’t fit.
      <cite>- Owner, Auto Industry</cite>
    </blockquote>
    <blockquote class="quote" style="left:42px;top:761px">
      The process changes we have made in recruiting as a result of working with Tallow Ridge’s RoleMatch have been transformational. We went into the interviews with confidence which ultimately made it easier to select the right candidate for the roles.<br>Thanks to your tools and assessments I have a stronger team!
      <cite>- VP, Oil &amp; Gas Sector</cite>
    </blockquote>
    <blockquote class="quote" style="left:404px;top:812px;width:305px">
      We’ve had very good success over the past year and a half since I’ve been in this role with reducing our turnover from around 50% to less than 10%. I feel very strongly that much of that has to do with our practice of only hiring people who are a match for our benchmarks.
      <cite>- Recruiter, IT Sector</cite>
    </blockquote>

    <footer class="brand-band brand-band--bottom">
      <div class="brand-name"><span class="mark"></span>TALLOW RIDGE</div>
      <dl class="contact">
        <dt>web</dt><dd>www.tallowridgeadvisory.com</dd>
        <dt>email</dt><dd>hello@tallowridgeadvisory.com</dd>
        <dt>phone</dt><dd>555 010 0199</dd>
      </dl>
    </footer>
  </section>

</div>
</body>
</html>
```